Start-Up Property Development Company Requires Word Press Website Design

A new property development company in Sydney requires a new website.
This version (Version 1) is very simple and will represent one, small aspect of what the company does, which is acquiring properties for redevelopment:

Needed:
- 1 page incorporating copy, logo and illustration.
- Email contact form.
- Contact information.

It will be expanded in the next few months to include another section for marketing homes for sale (Version 2). This section should sit on top of the Version 1 (in the top section of the same scrolling page).

So this initial design must be able to simply incorporate the expansion.

The site design needs to:
- Take up the entire width of the monitor.
- Not be too different from companies corporate look and feel.
- Be simple, functional and elegant.
- Have a long scroll (1 page) with navigation items at the top of the screen simply linking to the corresponding section lower in the page.

Reason: Not happy with the choice of designs. I'm wanting something clean and fresh and not too intensive with graphics.

```html
<!DOCTYPE html>
<html lang="en">
<head>
<meta charset="utf-8">
<title>Norvale Property</title>
<link href="https://fonts.googleapis.com/css2?family=Open+Sans:wght@400;600;700;800&family=Bitter:wght@700&display=swap" rel="stylesheet">
<style>
:root{
  --red:#e0232e;
  --red-dark:#b81a23;
  --ink:#111111;
  --nav:#1c1c1c;
  --panel:#5a5a5a;
  --grey:#8c8c8c;
  --light:#f4f4f4;
  --white:#ffffff;
}
*{box-sizing:border-box;margin:0;padding:0}
html,body{width:723px;height:1200px;overflow:hidden;background:var(--white)}
body{font-family:"Open Sans",Arial,sans-serif;color:var(--ink);position:relative}
.page{position:relative;width:723px;height:1200px}

/* header */
.site-header{position:absolute;top:0;left:0;width:723px;height:87px;display:flex;align-items:center;justify-content:space-between;padding:0 30px}
.brand{display:flex;align-items:center;gap:8px;font-weight:800;font-size:25px;line-height:1;color:var(--red);letter-spacing:-.3px}
.brand-mark{width:14px;height:14px;background:var(--red);border-radius:50%}
.header-phone{display:flex;align-items:center;gap:6px;font-size:13px;color:var(--ink)}

/* nav */
.main-nav{position:absolute;top:87px;left:0;width:723px;height:22px;background:var(--nav);display:flex;padding-left:78px}
.main-nav a{color:var(--white);text-decoration:none;font-size:9.5px;font-weight:700;padding:0 12px;line-height:22px;border-right:1px solid #333}
.main-nav a.active{background:var(--red)}

/* hero */
.hero{position:absolute;top:109px;left:0;width:723px;height:301px}
.hero-photo{position:absolute;inset:0;background:linear-gradient(180deg,#bcd1e2 0%,#d9d2c4 40%,#9a8f7c 75%,#5f6b3f 100%)}
.hero-caption{position:absolute;left:0;right:0;bottom:0;height:58px;background:rgba(0,0,0,.18);display:flex;align-items:center;justify-content:center;font-family:"Bitter",Georgia,serif;font-weight:700;font-size:22px;color:var(--white)}
.hero-arrow{position:absolute;top:128px;width:20px;height:36px;background:rgba(255,255,255,.7);display:flex;align-items:center;justify-content:center}
.hero-arrow.prev{left:0}.hero-arrow.next{right:0}

/* section titles */
.section-title{position:absolute;left:0;width:723px;text-align:center}
.section-title h2{font-size:24px;line-height:32px;font-weight:700;color:var(--red);letter-spacing:.5px;display:inline-flex;align-items:center;gap:14px}
.section-title h2::before,.section-title h2::after{content:"";width:150px;height:1px;background:#cfcfcf}
.dots{display:flex;justify-content:center;gap:6px;margin-top:6px}
.dots span{width:6px;height:6px;border-radius:50%;background:var(--ink)}
.dots span.on{background:var(--red)}

/* process */
.process{position:absolute;top:478px;left:0;width:723px;height:120px}
.step{position:absolute;top:0;width:96px;text-align:center}
.step-box{width:82px;height:82px;margin:0 auto;background:var(--ink);border-radius:10px;display:flex;align-items:center;justify-content:center}
.step-label{margin-top:14px;font-size:14px;font-weight:800;color:var(--ink)}
.step-arrow{position:absolute;top:35px}

/* welcome */
.welcome{position:absolute;top:610px;left:0;width:723px;height:192px}
.welcome-red{position:absolute;left:0;top:0;width:362px;height:192px;background:var(--red)}
.welcome-grey{position:absolute;left:362px;top:0;width:361px;height:192px;background:var(--panel)}
.welcome-video{position:absolute;left:87px;top:10px;width:262px;height:172px;background:linear-gradient(160deg,#9cb8cf 0%,#c9b79a 55%,#6d6a63 100%)}
.video-bar{position:absolute;left:0;right:0;bottom:0;height:22px;background:rgba(0,0,0,.7);display:flex;align-items:center;padding:0 8px;gap:8px}
.video-track{flex:1;height:4px;background:#777;position:relative}
.video-track::before{content:"";position:absolute;left:0;top:0;width:30%;height:4px;background:var(--red)}
.welcome-text{position:absolute;left:372px;top:12px;width:320px;color:var(--white)}
.welcome-text h3{font-size:16px;font-weight:700;margin-bottom:6px}
.welcome-text p{font-size:9px;line-height:1.55;color:#e4e4e4}
.read-more{display:inline-block;margin-top:10px;font-size:9px;font-weight:700;color:var(--white);background:var(--ink);padding:4px 8px}

/* gallery */
.gallery{position:absolute;top:872px;left:0;width:723px;height:104px}
.gallery-item{position:absolute;top:0;width:135px;height:104px}
.gallery-item.g1{left:82px;background:linear-gradient(170deg,#a9c3dc,#7f8f5e)}
.gallery-item.g2{left:228px;background:linear-gradient(170deg,#bcd0e0,#b49a74)}
.gallery-item.g3{left:374px;background:linear-gradient(170deg,#8fb3d8,#8b7561)}
.gallery-item.g4{left:520px;background:linear-gradient(170deg,#e3e3e3,#9a9fa4)}
.gallery-arrow{position:absolute;top:40px}

/* footer */
.site-footer{position:absolute;top:1000px;left:0;width:723px;height:200px;background:var(--ink);color:var(--white)}
.footer-col{position:absolute;top:14px}
.footer-col h4{font-size:13px;font-weight:700;margin-bottom:10px;display:flex;align-items:center;gap:6px}
.testimonial{left:72px;width:200px}
.quote-box{background:#2b2b2b;padding:10px 12px;font-size:8.5px;line-height:1.55;color:#cfcfcf;position:relative}
.quote-name{font-size:9px;font-weight:700;margin-top:6px;text-align:right;padding-right:16px}
.newsletter{left:308px;width:170px}
.newsletter p{font-size:9px;line-height:1.5;color:#cfcfcf;margin-bottom:8px}
.email-field{width:130px;height:18px;background:var(--white);font-size:8px;color:#888;padding:3px 6px;margin-bottom:6px}
.subscribe{display:inline-block;background:var(--red);font-size:9px;font-weight:700;padding:3px 9px}
.contact{left:520px;width:180px}
.contact-row{display:flex;gap:7px;font-size:9px;line-height:1.4;margin-bottom:10px;align-items:flex-start;color:#e6e6e6}
.contact-row.big{font-size:12px;font-weight:700;color:var(--white)}
.footer-bottom{position:absolute;left:0;bottom:0;width:723px;height:24px;border-top:1px solid #2d2d2d;display:flex;align-items:center;justify-content:space-between;padding:0 20px;font-size:8.5px;color:#bbb}
.social{display:flex;gap:5px}
.social span{width:12px;height:12px;border-radius:50%;background:#555}
</style>
</head>
<body>
<div class="page">

  <header class="site-header">
    <div class="brand"><span class="brand-mark"></span>Norvale Property</div>
    <div class="header-phone">
      <svg width="13" height="13" viewBox="0 0 24 24"><circle cx="12" cy="12" r="11" fill="none" stroke="#999" stroke-width="2"/><path d="M8 6l2 0 1 3-1.5 1a7 7 0 0 0 4.5 4.5l1-1.5 3 1 0 2c0 1-1 2-2 2A10 10 0 0 1 6 8c0-1 1-2 2-2z" fill="#999"/></svg>
      012-555-0148
    </div>
  </header>

  <nav class="main-nav">
    <a class="active">HOME</a><a>ABOUT US</a><a>WHAT WE DO</a><a>WORK GALLERY</a><a>OUR TEAM</a><a>TESTIMONIALS</a><a>CONTACT US</a>
  </nav>

  <section class="hero">
    <div class="hero-photo" role="img" aria-label="Photo of a happy family celebrating in front of their two-storey home"></div>
    <div class="hero-arrow prev"><svg width="8" height="12" viewBox="0 0 8 12"><path d="M7 1L2 6l5 5" stroke="#333" stroke-width="2" fill="none"/></svg></div>
    <div class="hero-arrow next"><svg width="8" height="12" viewBox="0 0 8 12"><path d="M1 1l5 5-5 5" stroke="#333" stroke-width="2" fill="none"/></svg></div>
    <div class="hero-caption">Lorem ipsum dolor sit amer consectetuer adipisem</div>
  </section>

  <div class="section-title" style="top:420px">
    <h2>WHAT WE DO</h2>
    <div class="dots"><span></span><span class="on"></span><span></span></div>
  </div>

  <section class="process">
    <div class="step" style="left:100px">
      <div class="step-box">
        <svg width="40" height="44" viewBox="0 0 40 44"><path d="M8 3h17l8 8v30H8z" fill="none" stroke="#fff" stroke-width="3"/><path d="M14 18h14M14 24h14M14 30h10" stroke="#fff" stroke-width="3"/><rect x="2" y="10" width="6" height="28" fill="var(--red)"/></svg>
      </div>
      <div class="step-label">ACQUIRE</div>
    </div>
    <svg class="step-arrow" style="left:204px" width="100" height="12" viewBox="0 0 100 12"><path d="M0 6h90" stroke="var(--red)" stroke-width="2" stroke-dasharray="3 3"/><path d="M90 1l8 5-8 5z" fill="var(--red)"/></svg>
    <div class="step" style="left:312px">
      <div class="step-box">
        <svg width="46" height="42" viewBox="0 0 46 42"><path d="M4 20L23 4l19 16" stroke="#fff" stroke-width="3" fill="none"/><path d="M10 18v20h26V18" stroke="#fff" stroke-width="3" fill="none"/><rect x="17" y="23" width="12" height="10" fill="var(--red)"/><path d="M20 26l6 6M26 26l-6 6" stroke="#fff" stroke-width="2"/></svg>
      </div>
      <div class="step-label">RE-DEVELOP</div>
    </div>
    <svg class="step-arrow" style="left:418px" width="100" height="12" viewBox="0 0 100 12"><path d="M0 6h90" stroke="var(--red)" stroke-width="2" stroke-dasharray="3 3"/><path d="M90 1l8 5-8 5z" fill="var(--red)"/></svg>
    <div class="step" style="left:524px">
      <div class="step-box">
        <svg width="46" height="42" viewBox="0 0 46 42"><path d="M3 22L21 6l18 16" stroke="#fff" stroke-width="3" fill="none"/><path d="M9 20v18h24V20" stroke="#fff" stroke-width="3" fill="none"/><path d="M26 18h14l4 6-4 6H26z" fill="var(--red)"/><circle cx="30" cy="24" r="2" fill="#fff"/></svg>
      </div>
      <div class="step-label">SALE</div>
    </div>
  </section>

  <section class="welcome">
    <div class="welcome-red"></div>
    <div class="welcome-grey"></div>
    <div class="welcome-video" role="img" aria-label="Video still of builders on site in front of a new house">
      <div class="video-bar">
        <svg width="8" height="10" viewBox="0 0 8 10"><path d="M0 0l8 5-8 5z" fill="#fff"/></svg>
        <div class="video-track"></div>
        <svg width="10" height="10" viewBox="0 0 10 10"><path d="M0 3h3l3-3v10L3 7H0z" fill="#fff"/></svg>
      </div>
    </div>
    <div class="welcome-text">
      <h3>Welcome to Norvale Property</h3>
      <p>Norvale Property sources well located homes and sites across Sydney, then plans and manages each redevelopment from purchase to handover. We work closely with owners, councils and builders to deliver quality housing that adds lasting value to every neighbourhood we build in.</p>
      <span class="read-more">READ MORE ›</span>
    </div>
  </section>

  <div class="section-title" style="top:818px">
    <h2>PROJECT GALLERY</h2>
    <div class="dots"><span></span><span class="on"></span><span></span></div>
  </div>

  <section class="gallery">
    <svg class="gallery-arrow" style="left:58px" width="12" height="20" viewBox="0 0 12 20"><path d="M10 2L2 10l8 8" stroke="#555" stroke-width="2.5" fill="none"/></svg>
    <div class="gallery-item g1" role="img" aria-label="Completed family home with front garden"></div>
    <div class="gallery-item g2" role="img" aria-label="Builders reviewing plans outside a house"></div>
    <div class="gallery-item g3" role="img" aria-label="Timber house frame under construction"></div>
    <div class="gallery-item g4" role="img" aria-label="Architectural model of a new home"></div>
    <svg class="gallery-arrow" style="left:664px" width="12" height="20" viewBox="0 0 12 20"><path d="M2 2l8 8-8 8" stroke="#555" stroke-width="2.5" fill="none"/></svg>
  </section>

  <footer class="site-footer">
    <div class="footer-col testimonial">
      <h4><svg width="12" height="12" viewBox="0 0 12 12"><circle cx="6" cy="4" r="3" fill="#fff"/><path d="M0 12a6 5 0 0 1 12 0z" fill="#fff"/></svg>Client Testimonials</h4>
      <div class="quote-box">“ Working with the team was simple from start to finish. They bought our old house quickly and kept us informed at every step. ”</div>
      <div class="quote-name">Daniel Hay</div>
    </div>
    <div class="footer-col newsletter">
      <h4>Subscribe to Newsletter</h4>
      <p>Get latest updates by entering your email address</p>
      <div class="email-field">Email Address</div>
      <span class="subscribe">Subscribe</span>
    </div>
    <div class="footer-col contact">
      <h4>Contact Information</h4>
      <div class="contact-row">
        <svg width="10" height="12" viewBox="0 0 10 12"><path d="M5 0a4 4 0 0 1 4 4c0 3-4 8-4 8S1 7 1 4a4 4 0 0 1 4-4z" fill="#fff"/></svg>
        <span>Norvale Pty Ltd<br>P.O. Box 82, Redfern<br>NSW 2016</span>
      </div>
      <div class="contact-row big">
        <svg width="12" height="12" viewBox="0 0 24 24"><path d="M6 2l4 0 2 5-3 2a12 12 0 0 0 6 6l2-3 5 2v4c0 2-2 3-3 3A18 18 0 0 1 3 5c0-1 1-3 3-3z" fill="#fff"/></svg>
        <span>012-555-0148</span>
      </div>
      <div class="contact-row">
        <svg width="12" height="10" viewBox="0 0 12 10"><rect x="0.5" y="0.5" width="11" height="9" fill="none" stroke="#fff"/><path d="M1 1l5 4 5-4" stroke="#fff" fill="none"/></svg>
        <span>info@norvale.com.au</span>
      </div>
    </div>
    <div class="footer-bottom">
      <span>© 2014 NorvaleProperty. All Rights Reserved</span>
      <div class="social"><span></span><span></span><span></span><span></span></div>
    </div>
  </footer>

</div>
</body>
</html>
```